Quote Cards With TK May 2025 for Instagram

I would like to put these quotes over one of the pictures attached; Instagram (new size: 4:5 (1080 x 1350 pixels) One Quote per picture, and I want the quote to be bold or easy to read as well. I provided a few reference graphics that I really like as examples below. In very small letters at the bottom add @TKBarlowOnline

All of the pictures are attached; you can pick any photo and add one quote to it; but no stock photography

```html
<!DOCTYPE html>
<html lang="en">
<head>
<meta charset="utf-8">
<title>Quote Cards With TK – May 2025</title>
<link href="https://fonts.googleapis.com/css2?family=Bebas+Neue&family=Poppins:ital,wght@0,400;0,600;0,700;1,500&family=Great+Vibes&display=swap" rel="stylesheet">
<style>
:root{
  --page:#ffffff;
  --ink:#1c1c1c;
  --white:#ffffff;
  --magenta:#f21ee8;
  --yellow:#f3e600;
  --pink-fix:#c81bd0;
  --shade:rgba(40,40,40,.82);
  --card-w:222px;
  --card-h:277px;
}
*{box-sizing:border-box;margin:0;padding:0}
html,body{width:1200px;height:595px;overflow:hidden;background:var(--page)}
.board{position:relative;width:1200px;height:595px}
.card{position:absolute;width:var(--card-w);height:var(--card-h);overflow:hidden;color:var(--white);font-family:"Poppins",sans-serif}
.photo{position:absolute;inset:0}
.handle{position:absolute;font-family:"Poppins",sans-serif;font-size:6px;font-weight:600;letter-spacing:.1px}
.bebas{font-family:"Bebas Neue",sans-serif;font-weight:400}

/* row positions */
.c1{left:16px;top:13px}.c2{left:252px;top:13px}.c3{left:489px;top:13px}.c4{left:725px;top:13px}.c5{left:962px;top:13px}
.c6{left:16px;top:302px}.c7{left:252px;top:302px}.c8{left:489px;top:302px}.c9{left:725px;top:302px}.c10{left:962px;top:302px}

/* card 1 */
.c1 .photo{background:linear-gradient(160deg,#d9d9d6 0%,#9e9c98 45%,#3a3634 100%)}
.c1 .panel{position:absolute;left:24px;top:104px;width:174px;height:131px;background:var(--shade);display:flex;align-items:center;justify-content:center;text-align:center;font-size:17px;line-height:18.5px;letter-spacing:.3px}
.c1 .handle{left:0;right:0;bottom:10px;text-align:center;font-size:7px}

/* card 2 */
.c2 .photo{background:linear-gradient(110deg,#111 0%,#1d1d1f 45%,#7d8ea0 75%,#b9c8d2 100%)}
.c2 .headline{position:absolute;left:14px;top:37px;font-size:36px;line-height:32.5px}
.c2 .accent{color:var(--magenta)}
.c2 .tag{position:absolute;left:106px;top:170px;width:116px;height:84px;background:var(--magenta);padding:7px 7px 0;font-size:14px;line-height:15.3px}
.c2 .tag .handle{position:static;display:block;font-size:5px;margin-top:3px}

/* card 3 */
.c3 .photo{background:linear-gradient(180deg,#c9dbe8 0%,#8a9a88 40%,#3b4530 75%,#1c1f17 100%)}
.c3 .copy{position:absolute;right:14px;top:128px;text-align:right}
.c3 .big{font-size:27px;line-height:25px}
.c3 .yes{color:var(--yellow);font-size:16px;line-height:18px;margin-top:1px}
.c3 .cta{font-size:15px;line-height:15.5px;margin-top:8px}
.c3 .cta span{color:var(--magenta)}
.c3 .handle{right:10px;bottom:13px;font-weight:400}

/* card 4 */
.c4 .photo{right:auto;width:84px;background:linear-gradient(180deg,#3c4e6a 0%,#1e2330 60%,#0e0e10 100%)}
.c4 .side{position:absolute;left:84px;top:0;right:0;bottom:0;background:linear-gradient(180deg,#c9a78a 0%,#cfc3b6 55%,#e4e0dc 100%)}
.c4 .quote{position:absolute;left:84px;right:0;top:77px;text-align:center;color:var(--ink);font-size:14px;line-height:15.5px;letter-spacing:.2px}
.c4 .handle{left:84px;right:0;top:204px;text-align:center;color:var(--ink);font-size:5px}

/* card 5 */
.c5 .photo{background:linear-gradient(180deg,#2e2521 0%,#1a1513 60%,#3a302b 100%)}
.c5 .box{position:absolute;left:26px;top:137px;width:168px;height:115px;background:linear-gradient(180deg,#ffffff 0%,#f6f0f4 60%,#e4c8e6 100%);color:var(--ink);text-align:center;padding-top:8px}
.c5 .box p{font-size:12.6px;line-height:17.5px;font-weight:600}
.c5 .box .handle{position:static;display:block;font-size:5px;margin-top:5px}

/* card 6 */
.c6 .photo{background:linear-gradient(90deg,#7a7a7a 0%,#c8c8c8 45%,#2d2d2d 100%)}
.c6 .veil{position:absolute;inset:0}
.c6 .quote{position:absolute;left:20px;top:140px;font-size:11.6px;line-height:14.6px}
.c6 .handle{left:20px;bottom:20px;font-size:5px}

/* card 7 */
.c7 .photo{background:radial-gradient(120% 80% at 30% 10%,#3a3a3a 0%,#1c1c1c 50%,#0c0c0c 100%)}
.c7 .copy{position:absolute;left:0;right:0;top:60px;text-align:center}
.c7 .lead{font-size:12px;line-height:15px;font-weight:400}
.c7 .script{font-family:"Great Vibes",cursive;font-size:32px;line-height:34px;margin-top:4px}
.c7 .word{font-size:22px;font-weight:700;letter-spacing:1px;line-height:24px;margin-top:4px}
.c7 .small{font-size:9px;line-height:11px}
.c7 .handle{left:0;right:0;bottom:23px;text-align:center;font-size:5px;font-weight:400}

/* card 8 */
.c8 .photo{background:linear-gradient(180deg,#141b3a 0%,#5a4a3a 35%,#b58a55 60%,#3a2a1e 100%)}
.c8 .copy{position:absolute;left:16px;top:118px}
.c8 .big{font-size:25px;line-height:23.5px}
.c8 .sub{font-size:12px;line-height:15px;margin-top:9px}
.c8 .handle{left:16px;bottom:15px;font-size:5px}

/* card 9 */
.c9 .photo{background:linear-gradient(180deg,#4f7d8c 0%,#9a8f9e 40%,#c08bb0 60%,#d9a430 85%,#5a4a1a 100%)}
.c9 .box{position:absolute;left:45px;top:83px;width:132px;height:118px;background:rgba(255,255,255,.94);color:var(--ink);text-align:center;padding-top:18px;font-size:12.2px;line-height:15.3px}
.c9 .box .handle{position:static;display:block;font-size:5px;margin-top:7px}

/* card 10 */
.c10 .photo{left:142px;background:linear-gradient(180deg,#6a2a6a 0%,#d4189b 55%,#7a1f6e 100%)}
.c10 .side{position:absolute;left:0;top:0;bottom:0;width:142px;background:linear-gradient(180deg,#e31fae 0%,#9b2a9c 45%,#4a2a6a 100%)}
.c10 .big{position:absolute;left:0;width:142px;top:52px;text-align:center;font-size:31px;line-height:28.5px}
.c10 .box{position:absolute;left:14px;top:142px;width:113px;height:92px;background:var(--white);color:var(--ink);text-align:center;padding-top:9px;font-size:10.2px;line-height:12.2px}
.c10 .box em{display:block;color:var(--pink-fix);font-style:italic;font-weight:500}
.c10 .box .handle{position:static;display:block;font-size:4.5px;margin-top:9px;font-weight:400}
</style>
</head>
<body>
<main class="board">

  <article class="card c1">
    <div class="photo" role="img" aria-label="Photo of TK posing in a bright kitchen"></div>
    <div class="panel bebas">TIRED. MOODY.<br>STUBBORN BELLY FAT.<br>YOUR HORMONES ARE<br>SCREAMING FOR HELP!<br>LET’S FIX THAT.</div>
    <span class="handle">@TKBarlowOnline</span>
  </article>

  <article class="card c2">
    <div class="photo" role="img" aria-label="Photo of TK smiling in a black top against a sky"></div>
    <h2 class="headline bebas">WHAT<br>WORKED<br><span class="accent">IN YOUR<br>30S</span><br>WON’T<br>WORK<br>NOW.</h2>
    <div class="tag bebas">HERE’S WHAT<br>ACTUALLY DOES.<br>DROP 30 POUNDS<br>IN 3 MONTHS.<span class="handle">@TKBarlowOnline</span></div>
  </article>

  <article class="card c3">
    <div class="photo" role="img" aria-label="Photo of TK in black outfit on a hillside overlook"></div>
    <div class="copy bebas">
      <div class="big">FLAT TUMMY<br>IN YOUR 40S?</div>
      <div class="yes">IT’S STILL POSSIBLE!</div>
      <div class="cta">COMMENT <span>BYE BELLY</span><br>TO GET THE 10 SECRETS<br>TO A FLATTER TUMMY</div>
    </div>
    <span class="handle">@TKBarlowOnline</span>
  </article>

  <article class="card c4">
    <div class="photo" role="img" aria-label="Photo of TK standing in a sheer black outfit by a city window"></div>
    <div class="side"></div>
    <p class="quote">This 90-day<br>plan helped<br>women over 40<br>slim down, get<br>a tiny waist and<br>feel sexy again.<br>You’re next.</p>
    <span class="handle">@TKBarlowOnline</span>
  </article>

  <article class="card c5">
    <div class="photo" role="img" aria-label="Photo of TK pointing down toward the text"></div>
    <div class="box">
      <p>You’re doing all the<br>“right” things, but<br>your belly won’t go<br>down?&nbsp; Here’s what<br>you haven’t tried.</p>
      <span class="handle">@TKBarlowOnline</span>
    </div>
  </article>

  <article class="card c6">
    <div class="photo" role="img" aria-label="Black and white photo of TK in a sheer striped top"></div>
    <svg class="veil" width="222" height="277" viewBox="0 0 222 277" aria-hidden="true">
      <defs>
        <linearGradient id="veilFade" x1="0" y1="0" x2="0" y2="1">
          <stop offset="0" stop-color="#9a7a86"/>
          <stop offset=".45" stop-color="#5a4a55"/>
          <stop offset="1" stop-color="#1e1e22"/>
        </linearGradient>
      </defs>
      <polygon points="0,0 68,0 165,277 0,277" fill="url(#veilFade)"/>
    </svg>
    <p class="quote">Bloating.<br>Muffin top.<br>Puffy waistline.<br>Your body’s<br>screaming for a<br>different kind<br>of fix. Here it is</p>
    <span class="handle">@TKBarlowOnline</span>
  </article>

  <article class="card c7">
    <div class="photo" role="img" aria-label="Dark close-up photo of TK in black"></div>
    <div class="copy">
      <p class="lead">This is the secret<br>women over 40 are<br>using to get snatched;<br>without starving.</p>
      <p class="script">Comment</p>
      <p class="word">SKINNY</p>
      <p class="small">to get the exact plan.</p>
    </div>
    <span class="handle">@TKBarlowOnline</span>
  </article>

  <article class="card c8">
    <div class="photo" role="img" aria-label="Photo of TK courtside at a basketball arena"></div>
    <div class="copy bebas">
      <div class="big">THE STUBBORN<br>BELLY FAT<br>AFTER 40?</div>
      <div class="sub">IT’S NOT ABOUT CALORIES;<br>IT’S ABOUT YOUR HORMONES.<br>HERE IS THE FIX!</div>
    </div>
    <span class="handle">@TKBarlowOnline</span>
  </article>

  <article class="card c9">
    <div class="photo" role="img" aria-label="Photo of TK in a pink outfit among sunflowers"></div>
    <div class="box bebas">YOUR BELLY ISN’T FAT...<br>IT’S HORMONAL. AND<br>HERE’S HOW TO FIX IT.<br>COMMENT HORMONES IF<br>NOTHING IS WORKING.<span class="handle">@TKBarlowOnline</span></div>
  </article>

  <article class="card c10">
    <div class="photo" role="img" aria-label="Photo of TK in a pink gown on stage"></div>
    <div class="side"></div>
    <h2 class="big bebas">THAT<br>STUBBORN<br>WEIGHT?</h2>
    <div class="box">It’s not your fault.<br>Your hormones are<br>to blame and you’re<br>not alone;<em>But there is a fix.</em><span class="handle">@TKBarlowOnline</span></div>
  </article>

</main>
</body>
</html>
```